Global Expert Network Firm needs business card design

We need business card design for a new company based in Seoul, South Korea called 'Corwell Insight Partners'. We recruit industry experts covering all countries and connect our client and recruited expert by phone, face-to-face meetings and etc. We are a global expert network firm that is focused on delivering high-quality experts to our clients throughout the world. Our clients include multinational corporations, global consulting firms, private equity firms, venture capital firms, asset management companies.
We have made new logo and please find attachment.(Please use new logo)
Target Market(s)
Global Consulting Firms, Investment Firms, Private Equity Firms, Venture Capital Firms.
Industry/Entity Type
Recruitment
Contact Information for Business Card
We need two Languages (English and Korean Version).
The front is Korean and the back is English version.
[The back] [English]
Company Name: Corwell Insight Partners, Inc.
CEO Name: Daniel Park
Address: #507, Hanbit Bldg, 82 Maebongsan-ro, Dobong-gu, Seoul, 01327, Korea
Tel. +82 2 718 4052
Fax. +82 2 864 1097
Mobile. +82 10 7264 8815
Email: daniel@corwellip.com
Web: www.corwellip.com
[The front] [Korean] => Described in same order as English version.
회사명: 코웰인사이트파트너스(주)
대표이사: 박도현
주소: 서울시 도봉구 매봉산로 82 한빛빌딩 507호
Tel. 02 718 4052
Fax. 02 864 1097
Mobile. 010 7264 8815
Web: www.corwellip.com
Look and feel
Each slider illustrates characteristics of the customer's brand and the style your logo design should communicate.

```html
<!DOCTYPE html>
<html lang="ko">
<head>
<meta charset="utf-8">
<title>Corwell Insight Partners — Business Card</title>
<link rel="stylesheet" href="https://fonts.googleapis.com/css2?family=Noto+Sans+KR:wght@400;500;700&display=swap">
<style>
  :root {
    --navy: #1f2461;
    --ink: #23285e;
    --paper: #ffffff;
    --paper-shade: #eeeff3;
    --backdrop: #d9dbe1;
    --rule: #8a8ea8;
  }
  * { margin: 0; padding: 0; box-sizing: border-box; }
  html, body {
    width: 1200px;
    height: 900px;
    overflow: hidden;
    background: var(--backdrop);
    font-family: "Noto Sans KR", sans-serif;
    color: var(--ink);
  }
  .card {
    position: absolute;
    left: 150px;
    top: 180px;
    width: 900px;
    height: 540px;
    border-radius: 36px;
    overflow: hidden;
    background: linear-gradient(160deg, var(--paper) 0%, var(--paper-shade) 100%);
    box-shadow: 0 10px 30px rgba(20, 24, 60, 0.18);
  }
  .card__band {
    position: absolute;
    left: 0;
    bottom: 0;
    width: 100%;
    height: 42px;
    display: flex;
    gap: 5px;
  }
  .card__band-segment { background: var(--navy); height: 100%; }
  .card__band-segment--short { width: 280px; }
  .card__band-segment--long { flex: 1; }

  .person {
    position: absolute;
    left: 72px;
    top: 56px;
  }
  .person__title,
  .person__name {
    font-size: 46px;
    font-weight: 700;
    line-height: 1.12;
    color: var(--navy);
  }
  .person__links {
    margin-top: 14px;
    font-size: 19px;
    line-height: 1.45;
  }
  .person__rule {
    width: 320px;
    height: 1.5px;
    background: var(--rule);
    margin: 12px 0 16px;
  }
  .contact-list { list-style: none; font-size: 20px; line-height: 1.55; }
  .contact-list__item { display: flex; align-items: center; gap: 10px; }
  .contact-list__icon { width: 20px; height: 20px; fill: none; stroke: var(--ink); stroke-width: 1.8; }

  .brand {
    position: absolute;
    right: 84px;
    top: 84px;
    display: flex;
    align-items: flex-start;
    gap: 18px;
  }
  .brand__square {
    width: 44px;
    height: 44px;
    background: var(--navy);
    margin-top: 8px;
  }
  .brand__name {
    font-size: 42px;
    font-weight: 500;
    line-height: 1.12;
    color: var(--navy);
  }

  .company {
    position: absolute;
    right: 84px;
    bottom: 82px;
    text-align: right;
  }
  .company__name { font-size: 24px; font-weight: 700; color: var(--navy); margin-bottom: 6px; }
  .company__address { font-size: 21px; line-height: 1.45; }
</style>
</head>
<body>
  <main class="card">
    <section class="person">
      <p class="person__title">대표이사</p>
      <p class="person__name">박도현</p>
      <div class="person__links">
        <p class="person__email">daniel@corwellip.com</p>
        <p class="person__web">www.corwellip.com</p>
      </div>
      <div class="person__rule"></div>
      <ul class="contact-list">
        <li class="contact-list__item">
          <svg class="contact-list__icon" viewBox="0 0 20 20" aria-hidden="true"><path d="M2 8c0-3 3-5 8-5s8 2 8 5l-3 1-1-2H6L5 9z"/><rect x="4" y="11" width="12" height="6" rx="1"/></svg>
          <span>+82 2 718 4052</span>
        </li>
        <li class="contact-list__item">
          <svg class="contact-list__icon" viewBox="0 0 20 20" aria-hidden="true"><rect x="5" y="2" width="10" height="6"/><rect x="2" y="8" width="16" height="9" rx="1"/><line x1="6" y1="13" x2="14" y2="13"/></svg>
          <span>+82 2 864 1097</span>
        </li>
        <li class="contact-list__item">
          <svg class="contact-list__icon" viewBox="0 0 20 20" aria-hidden="true"><rect x="3" y="4" width="14" height="13" rx="1"/></svg>
          <span>+82 10 7264 8815</span>
        </li>
      </ul>
    </section>

    <section class="brand">
      <div class="brand__square"></div>
      <p class="brand__name">Corwell<br>Insight<br>Partners</p>
    </section>

    <section class="company">
      <p class="company__name">코웰인사이트파트너스(주)</p>
      <p class="company__address">주소: 서울시 도봉구 매봉산로 82<br>한빛빌딩 507호</p>
    </section>

    <div class="card__band">
      <div class="card__band-segment card__band-segment--short"></div>
      <div class="card__band-segment card__band-segment--long"></div>
    </div>
  </main>
</body>
</html>
```